Web Design for non-profit, Nautical themed

We are developing a web design for a non-profit organization. They are:

a non-profit 501©3 educational and service organization, grounded in the recognition that active engagement of the arts through can be an entry into growth and transformation. Our purpose is to develop and offer events that support this creative process bringing outstanding presenters to our town.

They are located in a beautiful coastal town and the client would like a "nautical" theme. This would include

- color palette of blue, green, possibly brown/beige, and possibly some deep red colors as accents. There is a file attached with some color palette ideas, but you don't have to choose from colors here.

- soothing, calm, clean professional look

- something in the background image that would indicate the four directions. This could be a compass or something similar.

- the client really likes this website:
http://www.harbrowcollective.example/

Please see attached for:

- a basic sketch that shows the overall layout that we desire. Feel free to modify this slightly but not too much. File name is 01-sketch.psd

- placeholder content that can be used throughout your design

You can also use any of the stock photos found here:
http://www.pellumimages.example/search/lightbox/48207356#b9a2d71

Target Market(s)

Mainly white American women who are in their 40s or older. Professional, affluent, highly educated.

Industry/Entity Type

Nautical

Requirements
Must have
• - sidebar with event information. Each event should include date, headshot, title, brief description and a "Register" and "Read more" link. We don't have any real headshots so use ones from Internet for now.

- use the attached 01-sketch.psd file as your starting point.

```html
<!DOCTYPE html>
<html lang="en">
<head>
<meta charset="utf-8">
<title>Tidewater Dialogues</title>
<link rel="stylesheet" href="https://fonts.googleapis.com/css2?family=Arimo:wght@400;700&display=swap">
<style>
  :root {
    --navy: #0f3557;
    --nav-grey: #4d4d4d;
    --text-grey: #555555;
    --ink: #222222;
    --sidebar: #e6e6e6;
    --rule: #b8b8b8;
    --white: #ffffff;
    --photo-light: #e4e3e7;
    --photo-mid: #b3b2b8;
    --photo-dark: #8e8d94;
  }
  * { box-sizing: border-box; margin: 0; padding: 0; }
  html, body { width: 1200px; height: 1175px; overflow: hidden; background: var(--white); }
  body { position: relative; font-family: "Arimo", Arial, sans-serif; color: var(--text-grey); }

  .main-nav { position: absolute; top: 11px; left: 10px; width: 1179px; height: 38px; }
  .main-nav a {
    position: absolute; top: 0; height: 38px; line-height: 38px; text-align: center;
    background: var(--nav-grey); color: var(--white); text-decoration: none; font-size: 18px;
  }
  .main-nav a.current { background: var(--navy); font-weight: 700; }

  .brand-mark { position: absolute; left: 16px; top: 78px; width: 100px; height: 100px; background: var(--nav-grey); }
  .brand-name { position: absolute; left: 133px; top: 134px; font-size: 50px; line-height: 50px; color: var(--ink); font-weight: 400; white-space: nowrap; }

  .social { position: absolute; display: flex; gap: 6px; }
  .social span { display: block; width: 30px; height: 30px; border-radius: 4px; }
  .social .s1 { background: #2f7fc4; }
  .social .s2 { background: #c8382e; }
  .social .s3 { background: #2a5b8e; }

  .search { position: absolute; left: 953px; top: 151px; width: 236px; height: 28px; border: 1px solid #999; }
  .search span { position: absolute; left: 9px; top: 7px; font-size: 13px; color: #333; }
  .search svg { position: absolute; right: 6px; top: 4px; }

  .hero { position: absolute; left: 10px; top: 202px; width: 856px; height: 490px; }
  .hero-photo {
    width: 856px; height: 403px;
    background:
      radial-gradient(ellipse 55% 45% at 50% 62%, #f2f2f4 0%, rgba(242,242,244,0) 70%),
      radial-gradient(ellipse 40% 30% at 28% 18%, #f6f6f8 0%, rgba(246,246,248,0) 80%),
      linear-gradient(180deg, var(--photo-mid) 0%, var(--photo-light) 55%, var(--photo-dark) 100%);
  }
  .hero-arrows { position: absolute; left: 757px; top: 354px; display: flex; gap: 5px; }
  .hero-arrows span { width: 33px; height: 30px; background: var(--navy); display: flex; align-items: center; justify-content: center; }
  .hero-caption { height: 87px; background: var(--navy); padding: 16px 11px 0; color: #d8dde4; }
  .hero-caption h1 { color: var(--white); font-size: 21px; font-weight: 700; margin-bottom: 4px; }
  .hero-caption p { font-size: 16px; line-height: 19px; }
  .hero-caption strong { color: var(--white); }

  .column { position: absolute; top: 713px; width: 265px; }
  .column h2 { color: var(--navy); font-size: 21px; font-weight: 700; margin-bottom: 1px; }
  .column p { font-size: 14px; line-height: 14.85px; color: var(--text-grey); white-space: nowrap; }
  .divider { position: absolute; top: 738px; height: 232px; border-left: 1px dashed var(--rule); }

  .read-more {
    display: inline-block; background: var(--navy); color: var(--white); font-size: 10px;
    padding: 3px 11px; text-decoration: none; height: 17px; width: 81px; white-space: nowrap;
  }
  .column .read-more { position: absolute; top: 240px; left: 0; }

  .sidebar { position: absolute; left: 891px; top: 202px; width: 309px; height: 776px; background: var(--sidebar); }
  .sidebar h3 { color: var(--navy); font-size: 18px; font-weight: 400; position: absolute; left: 11px; }
  .join-input { position: absolute; left: 11px; top: 40px; width: 218px; height: 35px; border: 1px solid #bbb; background: #ececec; }
  .join-btn { position: absolute; left: 234px; top: 40px; width: 64px; height: 35px; background: var(--navy); color: var(--white); font-size: 16px; line-height: 35px; text-align: center; }
  .rule { position: absolute; left: 11px; width: 287px; border-top: 1px dashed var(--rule); }

  .event { position: absolute; left: 11px; width: 287px; }
  .event time { font-size: 13px; color: var(--ink); }
  .event-photo { position: absolute; top: 18px; left: 0; width: 114px; height: 136px; background: var(--white); border: 1px solid #c8c8c8; padding: 4px; }
  .event-photo div { width: 100%; height: 100%; }
  .tone-june { background: linear-gradient(180deg, #c9a46a 0%, #dcbfa0 45%, #b0876a 100%); }
  .tone-july { background: linear-gradient(180deg, #d9d6d2 0%, #c49a80 40%, #2a2a30 100%); }
  .tone-august { background: linear-gradient(180deg, #c49a62 0%, #e0c2a6 50%, #8a6a4e 100%); }
  .event p { position: absolute; top: 15px; left: 119px; width: 170px; font-size: 12px; line-height: 14.3px; color: var(--ink); white-space: nowrap; }
  .event .read-more { position: absolute; top: 135px; left: 119px; }

  .footer { position: absolute; left: 10px; top: 1007px; width: 1179px; height: 156px; background: var(--navy); color: var(--white); }
  .footer-nav { position: absolute; left: 34px; top: 48px; font-size: 13px; letter-spacing: 0.4px; white-space: nowrap; }
  .footer-nav span.sep { margin: 0 10px; }
  .footer-contact { position: absolute; left: 34px; top: 86px; font-size: 15px; display: flex; gap: 24px; align-items: center; white-space: nowrap; }
  .footer-contact div { display: flex; align-items: center; gap: 8px; }
  .footer-divider { position: absolute; left: 736px; top: 38px; height: 88px; border-left: 1px dashed #7f93a8; }
  .legal { position: absolute; left: 772px; top: 40px; font-size: 13px; line-height: 19px; white-space: nowrap; }
  .legal .sep { margin: 0 7px; }
  .footer .social { left: 772px; top: 84px; }
  .footer-brand {
    position: absolute; left: 887px; top: 80px; width: 86px; height: 34px; background: var(--white);
    color: var(--ink); font-size: 10px; line-height: 12px; text-align: center; padding-top: 5px; overflow: hidden;
  }
</style>
</head>
<body>

<nav class="main-nav">
  <a class="current" href="#" style="left:0;width:117px">HOME</a>
  <a href="#" style="left:123px;width:185px">CALENDAR</a>
  <a href="#" style="left:312px;width:185px">ABOUT US</a>
  <a href="#" style="left:502px;width:175px">DONATE</a>
  <a href="#" style="left:681px;width:294px">TRAVEL INFORMATION</a>
  <a href="#" style="left:980px;width:199px">CONTACT US</a>
</nav>

<header>
  <span class="brand-mark"></span>
  <span class="brand-name">Tidewater Dialogues</span>
  <div class="social" style="left:772px;top:149px">
    <span class="s1" aria-label="Social link"></span>
    <span class="s2" aria-label="Video link"></span>
    <span class="s3" aria-label="Network link"></span>
  </div>
  <div class="search">
    <span>SEARCH</span>
    <svg width="18" height="18" viewBox="0 0 18 18"><circle cx="7" cy="7" r="5.5" fill="none" stroke="#555" stroke-width="1.5"/><line x1="11" y1="11" x2="16" y2="16" stroke="#555" stroke-width="1.8"/></svg>
  </div>
</header>

<section class="hero">
  <div class="hero-photo" role="img" aria-label="Close-up photo of an open silver pocket compass on a soft grey surface"></div>
  <div class="hero-arrows">
    <span><svg width="12" height="14" viewBox="0 0 12 14"><polyline points="9,1 3,7 9,13" fill="none" stroke="#fff" stroke-width="2.5"/></svg></span>
    <span><svg width="12" height="14" viewBox="0 0 12 14"><polyline points="3,1 9,7 3,13" fill="none" stroke="#fff" stroke-width="2.5"/></svg></span>
  </div>
  <div class="hero-caption">
    <h1>CONVERSATIONS THAT COULD TRANSFORM YOUR LIFE</h1>
    <p><strong>Tidewater Dialogues</strong> is bringing together speakers from around the globe who are transforming our world.<br>Join us for an event that could change your life.</p>
  </div>
</section>

<section class="column" style="left:20px">
  <h2>ABOUT US</h2>
  <p>Some text here Some text here Some text<br>Some text here Some text here Some text<br>Some text here Some text here Some text<br>Some text here Some text here Some text<br>Some text here Some text here Some text<br>Some text here Some text here Some text<br>Some text here Some text here Some text<br>Some text here Some text here Some text<br>Some text here Some text here Some text<br>Some text here Some text here Some text<br>Some text here Some text here Some text<br>Some text here Some text here Some text<br>Some text here Some text here Some text<br>Some text here Some text here Some text</p>
  <a class="read-more" href="#">Read More...</a>
</section>
<div class="divider" style="left:293px"></div>
<section class="column" style="left:312px">
  <h2>OUR SPEAKERS</h2>
  <p>Some text here Some text here Some text<br>Some text here Some text here Some text<br>Some text here Some text here Some text<br>Some text here Some text here Some text<br>Some text here Some text here Some text<br>Some text here Some text here Some text<br>Some text here Some text here Some text<br>Some text here Some text here Some text<br>Some text here Some text here Some text<br>Some text here Some text here Some text<br>Some text here Some text here Some text<br>Some text here Some text here Some text<br>Some text here Some text here Some text<br>Some text here Some text here Some text</p>
  <a class="read-more" href="#">Read More...</a>
</section>
<div class="divider" style="left:584px"></div>
<section class="column" style="left:603px">
  <h2>ANNAPOLIS</h2>
  <p>Some text here Some text here Some text<br>Some text here Some text here Some text<br>Some text here Some text here Some text<br>Some text here Some text here Some text<br>Some text here Some text here Some text<br>Some text here Some text here Some text<br>Some text here Some text here Some text<br>Some text here Some text here Some text<br>Some text here Some text here Some text<br>Some text here Some text here Some text<br>Some text here Some text here Some text<br>Some text here Some text here Some text<br>Some text here Some text here Some text<br>Some text here Some text here Some text</p>
  <a class="read-more" href="#">Read More...</a>
</section>

<aside class="sidebar">
  <h3 style="top:15px">JOIN OUR MAILING LIST</h3>
  <div class="join-input"></div>
  <div class="join-btn">JOIN</div>
  <h3 style="top:97px">UPCOMING EVENTS</h3>
  <div class="rule" style="top:133px"></div>

  <article class="event" style="top:149px">
    <time>June 1, 2013</time>
    <div class="event-photo"><div class="tone-june" role="img" aria-label="Headshot of the June speaker"></div></div>
    <p>Some text here Some text here<br>Some text here Some text here<br>Some text here Some text here<br>Some text here Some text here<br>Some text here Some text here<br>Some text here Some text here<br>Some text here Some text here<br>Some text here Some text here</p>
    <a class="read-more" href="#">Read More...</a>
  </article>
  <div class="rule" style="top:325px"></div>

  <article class="event" style="top:344px">
    <time>July 1, 2013</time>
    <div class="event-photo"><div class="tone-july" role="img" aria-label="Headshot of the July speaker"></div></div>
    <p>Some text here Some text here<br>Some text here Some text here<br>Some text here Some text here<br>Some text here Some text here<br>Some text here Some text here<br>Some text here Some text here<br>Some text here Some text here<br>Some text here Some text here</p>
    <a class="read-more" href="#">Read More...</a>
  </article>
  <div class="rule" style="top:518px"></div>

  <article class="event" style="top:535px">
    <time>August 1, 2013</time>
    <div class="event-photo"><div class="tone-august" role="img" aria-label="Headshot of the August speaker"></div></div>
    <p>Some text here Some text here<br>Some text here Some text here<br>Some text here Some text here<br>Some text here Some text here<br>Some text here Some text here<br>Some text here Some text here<br>Some text here Some text here<br>Some text here Some text here</p>
    <a class="read-more" href="#">Read More...</a>
  </article>
  <div class="rule" style="top:709px"></div>
  <div class="rule" style="top:739px"></div>
</aside>

<footer class="footer">
  <div class="footer-nav">HOME<span class="sep">I</span>CALENDAR<span class="sep">I</span>ABOUT US<span class="sep">I</span>DONATE<span class="sep">I</span>TRAVEL INFORMATION<span class="sep">I</span>CONTACT</div>
  <div class="footer-contact">
    <div><svg width="14" height="20" viewBox="0 0 14 20"><circle cx="7" cy="8" r="5" fill="none" stroke="#fff" stroke-width="2.2"/><line x1="7" y1="13" x2="7" y2="19" stroke="#fff" stroke-width="2.2"/><line x1="7" y1="0" x2="7" y2="3" stroke="#fff" stroke-width="2"/></svg>your address here your address here</div>
    <div><svg width="16" height="16" viewBox="0 0 16 16"><path d="M3 1 L6 1 L7 5 L5 6.5 C6 9 7 10 9.5 11 L11 9 L15 10 L15 13 C15 14 14 15 13 15 C6 14 2 10 1 3 C1 2 2 1 3 1 Z" fill="#fff"/></svg>123 456 7890 123</div>
    <div><svg width="16" height="13" viewBox="0 0 16 13"><path d="M0 5 L8 0 L16 5 L16 13 L0 13 Z" fill="#fff"/><polyline points="0,5 8,10 16,5" fill="none" stroke="#0f3557" stroke-width="1.3"/></svg>info@youremail.com</div>
  </div>
  <div class="footer-divider"></div>
  <div class="legal">Copyright 2013&nbsp; www.tidewaterdialogues.example<br>All rights reserved.<span class="sep">I</span>Terms and Conditions<span class="sep">I</span>Privacy Policy</div>
  <div class="social">
    <span class="s1" aria-label="Social link"></span>
    <span class="s2" aria-label="Video link"></span>
    <span class="s3" aria-label="Network link"></span>
  </div>
  <div class="footer-brand">Tidewater<br>Dialogues</div>
</footer>

</body>
</html>
```